Zielgruppe
Wir sind ein mittelständisches Unternehmen was gerade am Wachsen ist.
Unsere Tätigkeiten sind:
Schadstoffsanierung, Abbruch, Rückbau, Entsorgung.
Unsere Zielgruppe ist jedermann/frau
Aufgabenstellung
Das unser Logo mit dabei ist.
Das Design sollte modern,elegant sein. Nicht so verspielt und bunt. Klar strukturiert aber dennoch aussagekräftig.
Unser Slogan ist „wenn Qualität entscheidet“und sollte auch mit verwendet werden.
Unsere Fahrzeuge sind: Molvar Quendel H2/L2

```html
<!DOCTYPE html>
<html lang="de">
<head>
<meta charset="utf-8">
<title>Orvek Haus und Bauservice – Fahrzeugbeschriftung</title>
<link rel="stylesheet" href="https://fonts.googleapis.com/css2?family=Open+Sans:ital,wght@0,400;0,600;0,700;1,700&display=swap">
<style>
  :root {
    --navy: #262a44;
    --red: #e03a3e;
    --white: #ffffff;
    --page: #eceef1;
    --line: #d5d8de;
  }
  * { margin: 0; padding: 0; box-sizing: border-box; }
  html, body { width: 1200px; height: 770px; overflow: hidden; }
  body {
    background: var(--page);
    font-family: "Open Sans", Arial, sans-serif;
    color: var(--navy);
    position: relative;
  }
  .wrap-panel {
    position: absolute;
    left: 50px; top: 170px;
    width: 1100px; height: 430px;
    background: var(--white);
    border: 1px solid var(--line);
    border-radius: 14px;
    overflow: hidden;
  }
  .wrap-shapes { position: absolute; inset: 0; }
  .brand {
    position: absolute;
    left: 120px; top: 96px;
    display: flex; flex-direction: column; align-items: flex-start;
  }
  .brand-row { display: flex; align-items: center; gap: 12px; }
  .brand-square { width: 36px; height: 36px; background: var(--red); }
  .brand-name {
    font-weight: 700; font-size: 60px; line-height: 1;
    color: var(--navy); letter-spacing: 1px;
  }
  .brand-sub {
    margin-top: 10px;
    font-weight: 700; font-size: 15px; letter-spacing: 0.5px;
    color: var(--navy);
  }
  .services {
    position: absolute;
    left: 389px; top: 90px;
    list-style: none;
  }
  .services li {
    position: relative;
    padding-left: 24px;
    font-weight: 700; font-size: 19px; line-height: 26px;
    color: var(--navy);
  }
  .services li + li { margin-top: 0; }
  .services li::before {
    content: "";
    position: absolute; left: 2px; top: 5px;
    width: 6px; height: 17px;
    background: var(--red);
    transform: skewX(-30deg);
  }
  .contact {
    position: absolute;
    left: 104px; top: 232px;
    color: var(--white);
    font-weight: 600; font-size: 17px; line-height: 26px;
  }
  .contact-row { display: flex; align-items: center; gap: 9px; }
  .contact-row svg { width: 14px; height: 14px; }
  .slogan {
    position: absolute;
    left: 360px; top: 246px;
    color: var(--white);
    font-weight: 700; font-style: italic; font-size: 25px;
  }
  .door-brand {
    position: absolute;
    left: 748px; top: 276px;
    display: flex; flex-direction: column; align-items: flex-start;
  }
  .door-brand .brand-name { font-size: 28px; }
  .door-brand .brand-square { width: 16px; height: 16px; }
  .door-brand .brand-row { gap: 6px; }
  .door-brand .brand-sub { font-size: 7px; margin-top: 4px; letter-spacing: 0.3px; }
</style>
</head>
<body>
  <section class="wrap-panel" aria-label="Seitenbeschriftung Molvar Quendel H2/L2">
    <svg class="wrap-shapes" width="1100" height="430" viewBox="0 0 1100 430" aria-hidden="true">
      <polygon class="corner-red" points="0,0 218,0 25,280 0,280" fill="var(--red)"/>
      <polygon class="contact-band" points="60,223 383,223 345,284 29,284" fill="var(--navy)"/>
      <polygon class="slogan-band" points="355,234 680,234 680,296 315,296" fill="var(--red)"/>
    </svg>

    <div class="brand">
      <div class="brand-row">
        <span class="brand-square"></span>
        <span class="brand-name">ORVEK</span>
      </div>
      <span class="brand-sub">HAUS UND BAUSERVICE</span>
    </div>

    <ul class="services">
      <li>Schadstoffsanierung</li>
      <li>Abbruch &amp; Rückbau</li>
      <li>Baureinigung &amp; Entsorgung</li>
      <li>nachhaltige Verwertung<br>und Recycling</li>
    </ul>

    <div class="contact">
      <div class="contact-row">
        <svg viewBox="0 0 24 24" aria-hidden="true"><path fill="currentColor" d="M6.6 10.8a15 15 0 0 0 6.6 6.6l2.2-2.2c.3-.3.7-.4 1-.2 1.1.4 2.3.6 3.6.6.6 0 1 .4 1 1V20c0 .6-.4 1-1 1A17 17 0 0 1 3 4c0-.6.4-1 1-1h3.5c.6 0 1 .4 1 1 0 1.2.2 2.4.6 3.6.1.3 0 .7-.2 1z"/></svg>
        <span>01 555 204 781</span>
      </div>
      <div class="contact-row">
        <svg viewBox="0 0 24 24" aria-hidden="true"><g fill="none" stroke="currentColor" stroke-width="2"><circle cx="12" cy="12" r="9"/><path d="M3 12h18M12 3c3 3 3 15 0 18M12 3c-3 3-3 15 0 18"/></g></svg>
        <span>www.orvek-bau.com</span>
      </div>
    </div>

    <p class="slogan">wenn Qualität entscheidet</p>

    <div class="door-brand">
      <div class="brand-row">
        <span class="brand-square"></span>
        <span class="brand-name">ORVEK</span>
      </div>
      <span class="brand-sub">HAUS UND BAUSERVICE</span>
    </div>
  </section>
</body>
</html>
```